Quillmere Surgical Clinic ,Perth- Australia

We need a letterhead for our surgical clinic , it needs to highlight all the relevant contact details and practice locations. needs to be eye catching, but remain professional.all the logos attached
clear contact details as follows

Surgeon name : Mr Tevin Oskard
Phone : 1300 482 917 - 0417 296 481
Fax : 08- 7524 3968
email : tevin@parvellaclinicgroup.com.au
www.parvellaclinicgroup.com.au

Consults from
1- Haldane Medical Centre - Level 3 - Suite 42.
9 Cotterill Vance Parade
Murdoch WA 6157

2- KBRT Mandurah Suites
54 Pellingham Road Mandurah 6214

Operates at :
Our Lady of Peace Murdoch Hospital
Doreen Whitcombe Hospital
Tarn Health Campus
Rookwell Hospital
Ravenfield Hopital
Our Lady of Peace Subiaco

Target Market(s)

General Practitioners (Family doctors)

Industry/Entity Type

Medical

Requirements
Must have
• all the logos attached
• clear contact details as follows
• Surgeon name : Mr Tevin Oskard
• Phone : 1300 482 917 - 0417 296 481
• Fax : 08- 7524 3968
• email : tevin@parvellaclinicgroup.com.au
• www.parvellaclinicgroup.com.au
• Consults from
• 1- Haldane Medical Centre - Level 3 - Suite 42.
• 9 Cotterill Vance Parade
• Murdoch WA 6157
• 2- KBRT Mandurah Suites
• 54 Pellingham Road Mandurah 6214
• Operates at :
• Our Lady of Peace Murdoch Hospital
• Doreen Whitcombe Hospital
• Tarn Health Campus
• Rookwell Hospital
• Ravenfield Hopital
• Our Lady of Peace Subiaco
Nice to have
• a surgical theme in the design , but remain professional
Should not have
• big chunky designs
• no photographs or diagrams of objects (ECG, or stethoscope ..ect)

```html
<!DOCTYPE html>
<html lang="en">
<head>
<meta charset="utf-8">
<title>Quillmere Surgical Clinic – Letterhead</title>
<link rel="stylesheet" href="https://fonts.googleapis.com/css2?family=Open+Sans:wght@400;600;700&display=swap">
<style>
  :root {
    --backdrop: #d9dadd;
    --paper: #f7f7f5;
    --ink: #2b2d33;
    --ink-soft: #4a4c52;
    --rule: #3a3c42;
    --accent-blue: #2f56c4;
    --accent-dark: #34363d;
    --watermark: #e3e3e1;
    --badge: #c9ccd4;
  }
  * { margin: 0; padding: 0; box-sizing: border-box; }
  html, body { width: 1200px; height: 763px; overflow: hidden; }
  body {
    background: var(--backdrop);
    font-family: "Open Sans", Arial, sans-serif;
    color: var(--ink);
    position: relative;
  }
  .letterhead {
    position: absolute;
    left: 345px; top: 21px;
    width: 510px; height: 721px;
    background: var(--paper);
    box-shadow: 0 4px 18px rgba(0,0,0,.18);
    overflow: hidden;
  }
  .header { position: absolute; left: 30px; top: 28px; }
  .surgeon-name { font-size: 20px; font-weight: 700; letter-spacing: .2px; }
  .contact-line { font-size: 7px; line-height: 9.5px; color: var(--ink-soft); }
  .contact-line .sep { margin: 0 4px; }
  .header-rule {
    position: absolute; left: 215px; right: 0; top: 62px;
    height: 1.5px; background: var(--rule);
  }
  .watermark {
    position: absolute; left: 155px; top: 230px;
    width: 200px; height: 200px;
    border: 14px solid var(--watermark); border-radius: 50%;
    display: flex; align-items: center; justify-content: center; text-align: center;
  }
  .watermark-name {
    font-size: 17px; font-weight: 700; line-height: 21px; color: var(--watermark);
  }
  .badge-row {
    position: absolute; left: 30px; top: 540px; right: 30px;
    display: flex; align-items: center; gap: 14px;
  }
  .badge { background: var(--badge); display: block; }
  .badge.round { border-radius: 50%; }
  .footer-rule { position: absolute; left: 30px; right: 30px; top: 568px; height: 1px; background: var(--rule); }
  .locations { position: absolute; left: 30px; top: 576px; right: 30px; display: flex; gap: 30px; }
  .location-group h2 { font-size: 7.5px; font-weight: 700; letter-spacing: .4px; margin-bottom: 3px; }
  .location-group ul { list-style: none; }
  .location-group li { font-size: 6.5px; line-height: 8.5px; color: var(--ink-soft); position: relative; padding-left: 8px; }
  .location-group li::before {
    content: ""; position: absolute; left: 0; top: 2.5px;
    width: 3.5px; height: 3.5px; border-radius: 50%; background: var(--ink);
  }
  .location-group.extra { padding-top: 28px; }
  .base-band { position: absolute; left: 0; bottom: 0; }
</style>
</head>
<body>
  <main class="letterhead">
    <header class="header">
      <h1 class="surgeon-name">Mr Tevin Oskard</h1>
      <p class="contact-line">Phone : 1300 482 917</p>
      <p class="contact-line">Phone : 0417 296 481<span class="sep">|</span>Fax : 08- 7524 3968</p>
      <p class="contact-line">tevin@parvellaclinicgroup.com.au</p>
      <p class="contact-line">www.parvellaclinicgroup.com.au</p>
    </header>
    <div class="header-rule"></div>

    <div class="watermark" aria-label="Quillmere Surgical Clinic">
      <span class="watermark-name">Quillmere<br>Surgical<br>Clinic</span>
    </div>

    <div class="badge-row" aria-label="Professional affiliations">
      <span class="badge" style="width:26px;height:14px"></span>
      <span class="badge" style="width:46px;height:16px"></span>
      <span class="badge round" style="width:16px;height:16px"></span>
      <span class="badge" style="width:26px;height:12px"></span>
      <span class="badge" style="width:40px;height:12px"></span>
      <span class="badge round" style="width:18px;height:18px"></span>
      <span class="badge" style="width:60px;height:10px"></span>
      <span class="badge" style="width:30px;height:16px"></span>
      <span class="badge" style="width:44px;height:14px"></span>
      <span class="badge" style="width:14px;height:18px"></span>
    </div>
    <div class="footer-rule"></div>

    <section class="locations">
      <div class="location-group">
        <h2>CONSULTS FROM</h2>
        <ul>
          <li>Haldane Medical Centre - Level 3 - Suite 42.<br>9 Cotterill Vance Parade, Murdoch WA 6157</li>
          <li>KBRT Mandurah Suites<br>54 Pellingham Road, Mandurah 6214</li>
        </ul>
      </div>
      <div class="location-group">
        <h2>OPERATES AT</h2>
        <ul>
          <li>Our Lady of Peace Murdoch Hospital</li>
          <li>Doreen Whitcombe Hospital</li>
          <li>Tarn Health Campus</li>
          <li>Rookwell Hospital</li>
        </ul>
      </div>
      <div class="location-group extra">
        <ul>
          <li>Ravenfield Hopital</li>
          <li>Our Lady of Peace Subiaco</li>
        </ul>
      </div>
    </section>

    <svg class="base-band" width="510" height="60" viewBox="0 0 510 60" aria-hidden="true">
      <polygon points="0,24 300,24 340,60 0,60" fill="var(--accent-blue)"/>
      <polygon points="300,24 510,24 510,60 340,60" fill="var(--accent-dark)"/>
      <polygon points="0,16 510,16 510,24 0,24" fill="var(--paper)"/>
    </svg>
  </main>
</body>
</html>
```